Business Card Design Project

A dual branded business card.

We have 2 business's: kiWave and kiWave360º. kiWave is an online education marketplace that helps students fid great courses and classes (from learn to surf, to vocational training courses).

kiWave360º is an agency that helps primarily vocational course providers with their online marketing and student enrolments.

Target Market(s)

Manager and Marketing Manager / CEOs of TAFE, University, Vocational Course Providers (RTOs)

Industry/Entity Type

Education

Requirements
Must have
• Brent Hollowell
CEO

7-19 Parker Lane, Torquay Vic 3228
Phone: 1300 508 914
Mobile: 0412 598 207
Email: brent@kiwave-example.com.au

Both Logos
Nice to have
• I nice way to combine the 2 brands which act as related but separate business's.

Essentially kiWave is a marketplace which enable schools to get more student leads through the kiWave.com.au platform.

kiWave360º is an agency where we deliver online marketing services including: Searchly / Friendlane PPC, SEO, Retargeting, Website Development and design, Student Enrolment Intelligence, and more... Essentially and online agency specifically servicing the education sector.

kiWave
Australia's Education Marketplace with over 2,500 Teachers and Schools Australia wide (subject to change)

kiWave360º
Digital Marketing Education (subject to change)

Should not have
• Not cluttered, not cheap looking, needs to have digital agency quality...

```html
<!DOCTYPE html>
<html lang="en">
<head>
<meta charset="utf-8">
<title>Lumora and Lumora Digital business cards</title>
<link rel="stylesheet" href="https://fonts.googleapis.com/css2?family=Open+Sans:wght@400;600;700;800&display=swap">
<style>
  :root {
    --backdrop: #6e3d22;
    --white: #ffffff;
    --black: #050505;
    --blue-deep: #1672a8;
    --blue-light: #3c9bd4;
    --green: #8cc63f;
    --ink: #3a3a3a;
    --brand-green: #7cc520;
    --card-edge: #8fbfe0;
  }
  * { box-sizing: border-box; margin: 0; padding: 0; }
  html, body { width: 1200px; height: 708px; overflow: hidden; }
  body {
    background: var(--backdrop);
    font-family: "Open Sans", Arial, sans-serif;
    position: relative;
  }
  .card {
    position: absolute;
    width: 455px;
    height: 260px;
    border-radius: 13px;
    overflow: hidden;
  }
  .card--back-light { left: 77px; top: 75px; background: var(--white); border: 1px solid #555; }
  .card--back-dark { left: 614px; top: 84px; background: var(--black); }
  .card--front-market { left: 102px; top: 387px; }
  .card--front-agency { left: 631px; top: 391px; }
  .card--front {
    background: linear-gradient(90deg, var(--blue-deep), var(--blue-light));
    border: 1px solid var(--card-edge);
  }

  .brand-area {
    position: absolute; left: 0; right: 0; top: 0; height: 126px;
    display: flex; align-items: center; justify-content: center;
  }
  .brand-name {
    font-weight: 800;
    font-size: 54px;
    letter-spacing: -1px;
    line-height: 1;
    white-space: nowrap;
    display: flex; align-items: center; gap: 12px;
  }
  .brand-name--long { font-size: 44px; }
  .brand-name--green { color: var(--brand-green); }
  .brand-name--white { color: var(--white); }
  .brand-dot { width: 16px; height: 16px; border-radius: 50%; background: var(--brand-green); flex: none; }

  .contact-band {
    position: absolute; left: 0; right: 0; top: 129px; height: 89px;
    background: linear-gradient(90deg, var(--blue-deep), var(--blue-light));
    border-top: 2px solid var(--green);
    border-bottom: 2px solid var(--green);
    box-shadow: 0 -3px 0 var(--white), 0 3px 0 var(--white);
    color: var(--white);
    font-size: 12px;
    line-height: 16.5px;
  }
  .card--back-dark .contact-band { box-shadow: 0 -3px 0 var(--black), 0 3px 0 var(--black); }
  .address { position: absolute; right: 261px; top: 25px; text-align: right; white-space: nowrap; }
  .divider {
    position: absolute; left: 206px; top: 24px; width: 1px; height: 36px;
    background: rgba(255,255,255,0.75);
  }
  .contact-list { position: absolute; left: 218px; top: 17px; list-style: none; white-space: nowrap; }
  .contact-list li { display: flex; align-items: center; gap: 6px; }
  .contact-list svg { width: 9px; height: 9px; fill: var(--white); flex: none; }

  .person {
    position: absolute; left: 0; right: 0; top: 228px;
    text-align: center; font-size: 14.5px; letter-spacing: 1px;
    color: var(--ink);
  }
  .card--back-dark .person { color: var(--white); }
  .person strong { font-weight: 700; }

  .card--front .brand-area { top: 0; bottom: 0; height: auto; }
  .card--front .brand-name { font-size: 62px; }
  .card--front .brand-name--long { font-size: 50px; }
</style>
</head>
<body>

<section class="card card--back-light" aria-label="Lumora card back">
  <div class="brand-area">
    <span class="brand-name brand-name--green"><span class="brand-dot"></span>Lumora</span>
  </div>
  <div class="contact-band">
    <p class="address">7-19 Parker Lane<br>Larkfield Vic 3917</p>
    <span class="divider"></span>
    <ul class="contact-list">
      <li><svg viewBox="0 0 10 10"><path d="M2 0.5l2 2-1 1.2c.6 1.3 1.6 2.3 2.9 2.9L7 5.6l2 2-1 1.8C4 9.4.6 6 .6 2z"/></svg>1300 508 914</li>
      <li><svg viewBox="0 0 10 10"><rect x="2.5" y="0.5" width="5" height="9" rx="1"/></svg>0412 598 207</li>
      <li><svg viewBox="0 0 10 10"><path d="M0.5 3.5L5 0.8l4.5 2.7V9H0.5z"/></svg>brent@lumora-example.com.au</li>
    </ul>
  </div>
  <p class="person"><strong>Brent Hollowell,</strong> CEO</p>
</section>

<section class="card card--back-dark" aria-label="Lumora Digital card back">
  <div class="brand-area">
    <span class="brand-name brand-name--green brand-name--long"><span class="brand-dot"></span>Lumora Digital</span>
  </div>
  <div class="contact-band">
    <p class="address">7-19 Parker Lane<br>Larkfield Vic 3917</p>
    <span class="divider"></span>
    <ul class="contact-list">
      <li><svg viewBox="0 0 10 10"><path d="M2 0.5l2 2-1 1.2c.6 1.3 1.6 2.3 2.9 2.9L7 5.6l2 2-1 1.8C4 9.4.6 6 .6 2z"/></svg>1300 508 914</li>
      <li><svg viewBox="0 0 10 10"><rect x="2.5" y="0.5" width="5" height="9" rx="1"/></svg>0412 598 207</li>
      <li><svg viewBox="0 0 10 10"><path d="M0.5 3.5L5 0.8l4.5 2.7V9H0.5z"/></svg>brent@lumora-example.com.au</li>
    </ul>
  </div>
  <p class="person"><strong>Brent Hollowell,</strong> CEO</p>
</section>

<section class="card card--front card--front-market" aria-label="Lumora card front">
  <div class="brand-area">
    <span class="brand-name brand-name--white"><span class="brand-dot"></span>Lumora</span>
  </div>
</section>

<section class="card card--front card--front-agency" aria-label="Lumora Digital card front">
  <div class="brand-area">
    <span class="brand-name brand-name--white brand-name--long"><span class="brand-dot"></span>Lumora Digital</span>
  </div>
</section>

</body>
</html>
```